Flyer-Design für Tanzschule
Zielgruppe
Tanzschule
Aufgabenstellung
Ich möchte ein Banner zur Werbung auf Plaudernetz für eine Tanzveranstaltung so oder so ähnlich wie dieses Bild bildschirmfoto_2022_08_03_um_02.35.52.png.
Eines (oder mehrere) dieser Bilder sollte anstelle der Personen sein:
Der DJ sollte in Klein mit darauf:
bild_bernhard_dj.jpg (DJ Bernhard)
Folgende Logos sollen mit darauf. (Wichtigstes als erstes)
bildschirmfoto_2022_08_04_um_15.39.02.png (Original ohne weißen Hintergrund kann ich nachträglich darauf setzen. Ich habe es aktuell noch nicht)
Folgende Informationen sollen enthalten sein. (Wichtigste als erstes)
Bachata, Kizomba & Salsa Fiesta
Jeden Mittwoch 21:00 - 01:00 Uhr
La Nube - Ahornweg 7, 79102 Freiburg im Breisgau
5€ Verzehrbon / Kein Eintritt

```html
<!DOCTYPE html>
<html lang="de">
<head>
<meta charset="utf-8">
<title>Bachata Kizomba Salsa Fiesta – Banner</title>
<link rel="stylesheet" href="https://fonts.googleapis.com/css2?family=Kaushan+Script&family=Oswald:wght@300;500;600&display=swap">
<style>
  :root {
    --page: #ffffff;
    --grey: #c9c8c8;
    --peach: #e9b39a;
    --orange: #ee9a66;
    --gold: #f0bb4c;
    --coral: #f0606a;
    --yellow: #f6c431;
    --white: #ffffff;
    --brown: #6e4414;
  }
  html, body {
    margin: 0;
    width: 1200px;
    height: 960px;
    overflow: hidden;
    background: var(--page);
    font-family: "Oswald", sans-serif;
  }
  p, h1, h2 { margin: 0; }
  .banner {
    position: absolute;
    left: 74px;
    top: 184px;
    width: 1052px;
    height: 592px;
    overflow: hidden;
    background: linear-gradient(180deg, var(--grey) 0%, #d4c6bb 55%, var(--gold) 100%);
  }
  .banner__shapes { position: absolute; inset: 0; }
  .photo { position: absolute; }
  .photo--dj {
    left: 0; top: 0; width: 172px; height: 145px;
    border-radius: 0 0 90px 0 / 0 0 80px 0;
    background: linear-gradient(135deg, #6a4a8e 0%, #c86ad0 55%, #3a2a6a 100%);
    box-shadow: 6px 6px 0 var(--gold);
  }
  .photo--couple {
    left: 250px; top: 40px; width: 380px; height: 552px;
    border-radius: 180px 180px 0 0;
    background: radial-gradient(ellipse at 50% 40%, #fff8ec 0%, #f3dcc0 45%, rgba(236,200,150,0) 75%);
  }
  .dj-credit {
    position: absolute; left: 20px; top: 152px;
    font-weight: 500; font-size: 25px; line-height: 1;
    text-transform: uppercase; color: var(--white);
  }
  .dj-credit span { display: block; color: var(--coral); margin-top: 1px; }
  .schedule {
    position: absolute; left: 654px; top: 44px;
    font-weight: 300; font-size: 25px; line-height: 1; letter-spacing: -0.5px;
    text-transform: uppercase; color: var(--white); white-space: nowrap;
  }
  .schedule strong { font-weight: 600; color: var(--coral); }
  .headline {
    font-weight: 600; text-transform: uppercase; color: var(--white);
  }
  .headline span {
    position: absolute; left: 648px; line-height: 1; white-space: nowrap;
  }
  .headline .line-1 { top: 67px;  font-size: 100px; letter-spacing: -3px; }
  .headline .line-2 { top: 167px; font-size: 100px; letter-spacing: -3px; }
  .headline .line-3 { top: 254px; font-size: 142px; letter-spacing: -3px; }
  .brush-stroke { position: absolute; left: 0; top: 0; }
  .fiesta {
    position: absolute; left: 712px; top: 398px;
    font-family: "Kaushan Script", cursive;
    font-size: 104px; line-height: 1.3; padding: 0 10px;
    background: linear-gradient(135deg, var(--coral) 0%, #f2923f 45%, var(--yellow) 100%);
    -webkit-background-clip: text; background-clip: text;
    color: transparent;
  }
  .venue { position: absolute; left: 21px; top: 420px; color: var(--white); text-transform: uppercase; }
  .venue__name { font-weight: 500; font-size: 36px; line-height: 1; color: var(--coral); }
  .venue__address { margin-top: 8px; font-weight: 300; font-size: 21px; line-height: 1; }
  .venue__offer { margin-top: 8px; font-weight: 500; font-size: 16px; line-height: 1; }
  .partner { position: absolute; color: var(--brown); font-weight: 500; }
  .partner--bar { left: 28px; top: 524px; font-size: 11px; display: flex; flex-direction: column; align-items: center; gap: 6px; }
  .partner--bar::before {
    content: ""; width: 30px; height: 30px; border-radius: 50%;
    background: var(--brown); opacity: 0.85;
  }
  .partner--school { left: 138px; top: 538px; font-size: 15px; line-height: 1.1; }
</style>
</head>
<body>
  <main class="banner">
    <svg class="banner__shapes" width="1052" height="592" viewBox="0 0 1052 592" aria-hidden="true">
      <path d="M0 140 C90 160 180 140 180 190 C180 250 150 260 110 300 C60 360 50 380 0 375 Z" fill="var(--peach)" opacity="0.7"/>
      <path d="M700 592 C690 520 700 470 760 440 C830 400 860 300 920 230 C960 180 950 110 1052 80 L1052 592 Z" fill="var(--peach)" opacity="0.6"/>
      <path d="M650 592 C650 540 690 480 780 470 C880 455 930 380 1052 360 L1052 592 Z" fill="var(--orange)" opacity="0.75"/>
      <path d="M0 592 L0 520 C80 500 150 560 260 530 C380 500 520 540 650 592 Z" fill="var(--gold)" opacity="0.7"/>
    </svg>

    <div class="photo photo--dj" role="img" aria-label="Foto von DJ Bernhard mit Kopfhörern am DJ-Pult"></div>
    <p class="dj-credit">DJ Bernhard<span>Live</span></p>

    <div class="photo photo--couple" role="img" aria-label="Tanzpaar in einer Bachata-Figur mit Lichtspuren"></div>

    <p class="schedule">Jeden Mittwoch <strong>21:00 - 01:00 Uhr</strong></p>
    <h1 class="headline">
      <span class="line-1">Bachata</span>
      <span class="line-2">Kizomba</span>
      <span class="line-3">Salsa</span>
    </h1>
    <svg class="brush-stroke" width="1052" height="592" viewBox="0 0 1052 592" aria-hidden="true">
      <path d="M954 402 C880 404 760 410 700 432 C676 442 690 452 730 458" fill="none" stroke="var(--coral)" stroke-width="5" stroke-linecap="round"/>
    </svg>
    <p class="fiesta">Fiesta</p>

    <section class="venue">
      <h2 class="venue__name">La Nube</h2>
      <p class="venue__address">Ahornweg 7, 79102 Freiburg im Breisgau</p>
      <p class="venue__offer">5€ Verzehrbon / Kein Eintritt</p>
    </section>

    <div class="partner partner--bar">STIERHOF</div>
    <div class="partner partner--school">Tanzschule<br>Ritmo Vivo</div>
  </main>
</body>
</html>
```